Voren Spark Services requires a modern & sharp looking sign.

We need a sign to be designed for a local soccer club ground where advertising will take place. Text needs to be limited with only the basic information such as the logo/company name, website and mobile number. The EC40293 number must be placed somewhere in the sign.

The design should be similar to the flyer design attached, but in a more plain looking version.

Signage dimensions are 2050mm Wide x 900mm High.

Industry/Entity Type

Electrician

Requirements
Must have
• Logo/Company Name
• EC Number
• Website (www.vorenspark.com.au)
• Phone Number
• - SAME COLOR SCHEME AS THE LOGO
• - SAME LIGHTNING BOLT TO THE RIGHT OF THE SIGN (REFER TO FLYER)
Should not have
• NO PICTURES

```html
<!DOCTYPE html>
<html lang="en">
<head>
<meta charset="utf-8">
<title>Voren Spark Services – Ground Sign</title>
<link rel="stylesheet" href="https://fonts.googleapis.com/css2?family=Michroma&family=Open+Sans:wght@400&display=swap">
<style>
  :root {
    --backdrop: #262626;
    --sign-white: #f4f5f6;
    --brand-blue: #3a4ea3;
    --band-dark: #6b6c6e;
    --band-light: #d9dadb;
    --text-white: #ffffff;
    --licence-grey: #6d6e70;
  }
  html, body {
    margin: 0;
    padding: 0;
    width: 1200px;
    height: 1000px;
    overflow: hidden;
    background: var(--backdrop);
  }
  .canvas {
    display: block;
    width: 1200px;
    height: 1000px;
  }
  .sign-panel { fill: var(--sign-white); }
  .band-stop-dark { stop-color: var(--band-dark); }
  .band-stop-light { stop-color: var(--band-light); }
  .brand-mark { fill: var(--brand-blue); }
  .brand-name {
    font-family: "Michroma", sans-serif;
    font-size: 34px;
    fill: var(--brand-blue);
  }
  .licence-number {
    font-family: "Open Sans", sans-serif;
    font-size: 15px;
    fill: var(--licence-grey);
  }
  .tagline {
    font-family: "Michroma", sans-serif;
    font-size: 40px;
    fill: var(--text-white);
  }
  .tagline-accent { fill: var(--brand-blue); }
  .contact {
    font-family: "Michroma", sans-serif;
    font-size: 24px;
    fill: var(--brand-blue);
  }
</style>
</head>
<body>
<svg class="canvas" viewBox="0 0 1200 1000" xmlns="http://www.w3.org/2000/svg" role="img" aria-label="Voren Spark Services sign: Your trusted electrical contractor">
  <defs>
    <linearGradient id="band-metal" x1="0" y1="0" x2="0" y2="1">
      <stop offset="0" class="band-stop-dark"/>
      <stop offset="0.5" class="band-stop-light"/>
      <stop offset="1" class="band-stop-dark"/>
    </linearGradient>
  </defs>

  <g class="sign">
    <rect class="sign-panel" x="137" y="292" width="965" height="428"/>

    <g class="brand">
      <circle class="brand-mark" cx="412" cy="386" r="48"/>
      <text class="brand-name" x="480" y="400" textLength="412" lengthAdjust="spacingAndGlyphs">VOREN SPARK SERVICES</text>
    </g>

    <text class="licence-number" x="1090" y="322" text-anchor="end">EC40293</text>

    <rect class="tagline-band" x="137" y="485" width="965" height="128" fill="url(#band-metal)"/>
    <text class="tagline" x="610" y="538" text-anchor="middle" textLength="505" lengthAdjust="spacingAndGlyphs">YOUR <tspan class="tagline-accent">TRUSTED</tspan></text>
    <text class="tagline" x="618" y="594" text-anchor="middle" textLength="865" lengthAdjust="spacingAndGlyphs">ELECTRICAL CONTRACTOR</text>

    <text class="contact contact-phone" x="148" y="692" textLength="350" lengthAdjust="spacingAndGlyphs">TEL 0412 345 678</text>
    <text class="contact contact-web" x="1092" y="692" text-anchor="end" textLength="555" lengthAdjust="spacingAndGlyphs">WWW.VORENSPARK.COM.AU</text>
  </g>
</svg>
</body>
</html>
```